Harbourline Advisory Group - Business card design needed

I wish to get business cards designed so that it follows my website design ... http://www.harbourline-advisory.org
I need logos for KESTRA 4 and QV Network Affiliate for myself which I have uploaded the files.
I wish my qualifications PhD PMP FAICD to be smaller print than my name.
Regards
Lionel
Business
Contact Information for Business Card
Harbourline Advisory Group
Dr Lionel Harte PhD PMP FAICD
Director
PO Box 318 Kelmscott NSW 2193 AUSTRALIA
T:+61 2 9362 5047 M:+61 433 718520 F: +61 2 9381 6200
Email: lionel.harte@harbourline-advisory.org
Website: http://www.harbourline-advisory.org

```html
<!DOCTYPE html>
<html lang="en">
<head>
<meta charset="utf-8">
<title>Harbourline Advisory Group – Business Card</title>
<link rel="stylesheet" href="https://fonts.googleapis.com/css2?family=Source+Sans+3:wght@400;600;700&display=swap">
<style>
  :root {
    --page-bg: #d9dde2;
    --navy-deep: #0c1746;
    --navy-mid: #16266a;
    --navy-light: #24388a;
    --arc: rgba(120, 150, 220, 0.35);
    --text-main: #ffffff;
    --text-soft: #c9d3ee;
    --rule: rgba(150, 170, 220, 0.35);
    --icon: #7fa6e6;
    --badge-green: #1f8a5a;
    --badge-blue: #1ea0dc;
    --emblem-a: #b9d6f2;
    --emblem-b: #3d6db8;
  }
  * { box-sizing: border-box; margin: 0; padding: 0; }
  html, body { width: 1200px; height: 900px; overflow: hidden; }
  body {
    background: var(--page-bg);
    font-family: "Source Sans 3", "Myriad Pro", Arial, sans-serif;
    position: relative;
  }
  .card {
    position: absolute;
    left: 280px;
    width: 640px;
    height: 366px;
    border-radius: 6px;
    overflow: hidden;
    background: radial-gradient(ellipse at 60% 85%, var(--navy-light) 0%, var(--navy-mid) 45%, var(--navy-deep) 100%);
    box-shadow: 0 6px 18px rgba(0, 0, 0, 0.25);
    color: var(--text-main);
  }
  .card--front { top: 56px; }
  .card--back { top: 478px; }
  .card__arc { position: absolute; inset: 0; }
  .emblem {
    position: absolute;
    width: 68px;
    height: 72px;
    border-radius: 14px;
    background: radial-gradient(circle at 45% 45%, var(--emblem-a) 0%, var(--emblem-b) 55%, rgba(22, 38, 106, 0) 80%);
  }
  .card--front .emblem { left: 30px; top: 22px; }
  .company-name {
    position: absolute;
    font-size: 21px;
    font-weight: 600;
    line-height: 29px;
    color: var(--text-soft);
  }
  .card--front .company-name { left: 110px; top: 28px; }
  .card--back .company-name { right: 100px; top: 40px; text-align: left; font-size: 17px; line-height: 20px; }
  .card--back .emblem { right: 30px; top: 36px; width: 60px; height: 54px; }
  .rule {
    position: absolute;
    left: 30px; right: 30px; top: 188px;
    height: 1px;
    background: var(--rule);
  }
  .person { position: absolute; left: 40px; top: 192px; }
  .person__name { font-size: 25px; font-weight: 700; letter-spacing: 0.2px; }
  .person__quals { font-size: 11px; font-weight: 600; color: var(--text-soft); margin-left: 3px; vertical-align: 10px; }
  .person__title { font-size: 15px; font-weight: 700; margin-top: -4px; }
  .contact-divider {
    position: absolute;
    left: 210px; top: 236px;
    width: 1px; height: 96px;
    background: var(--rule);
  }
  .contact-list {
    position: absolute;
    list-style: none;
    font-size: 13.5px;
    color: var(--text-soft);
  }
  .contact-list li { display: flex; align-items: center; gap: 8px; height: 22px; }
  .contact-list--phones { left: 40px; top: 252px; font-size: 14.5px; }
  .contact-list--phones li { height: 25px; }
  .contact-list--web { left: 230px; top: 240px; font-size: 12.5px; }
  .icon { width: 13px; height: 13px; flex: none; fill: var(--icon); }
  .badge { position: absolute; }
  .badge--certification {
    left: 60px; top: 146px;
    width: 200px; height: 52px;
    border-radius: 26px;
    background: var(--badge-green);
  }
  .badge--partner {
    left: 44px; top: 226px;
    width: 150px; height: 38px;
    border-radius: 3px;
    background: var(--badge-blue);
  }
</style>
</head>
<body>

<section class="card card--front" aria-label="Business card front">
  <svg class="card__arc" width="640" height="366" viewBox="0 0 640 366" aria-hidden="true">
    <path d="M30 180 C 180 90, 400 60, 640 88" fill="none" stroke="var(--arc)" stroke-width="2"/>
    <path d="M30 186 C 190 100, 410 72, 640 96" fill="none" stroke="rgba(120,150,220,0.15)" stroke-width="6"/>
  </svg>
  <div class="emblem" role="img" aria-label="Company emblem image"></div>
  <div class="company-name">Harbourline Advisory<br>Group</div>
  <div class="rule"></div>
  <div class="person">
    <div><span class="person__name">Dr. Lionel Harte</span><span class="person__quals">PhD PMP FAICD</span></div>
    <div class="person__title">Director</div>
  </div>
  <div class="contact-divider"></div>
  <ul class="contact-list contact-list--phones">
    <li><svg class="icon" viewBox="0 0 16 16"><path d="M3 1l3 3-1.5 2a9 9 0 0 0 5.5 5.5L12 10l3 3-2 2.5C7 15 1 9 .5 3z"/></svg>+61-433-718520</li>
    <li><svg class="icon" viewBox="0 0 16 16"><rect x="1" y="2" width="5" height="13" rx="1"/><rect x="7" y="4" width="8" height="11" rx="1"/></svg>+61-2-9362-5047</li>
    <li><svg class="icon" viewBox="0 0 16 16"><rect x="4" y="1" width="8" height="5"/><rect x="1" y="6" width="14" height="6" rx="1"/><rect x="4" y="10" width="8" height="5"/></svg>+61-2-9381-6200</li>
  </ul>
  <ul class="contact-list contact-list--web">
    <li><svg class="icon" viewBox="0 0 16 16"><path d="M1 3h14v10H1z M1 3l7 6 7-6" fill="var(--icon)" stroke="var(--navy-deep)" stroke-width="1"/></svg>lionel.harte@harbourline-advisory.org</li>
    <li><svg class="icon" viewBox="0 0 16 16"><circle cx="8" cy="8" r="7"/><path d="M1 8h14M8 1v14M3 4h10M3 12h10" stroke="var(--navy-deep)" stroke-width="1" fill="none"/></svg>www.harbourline-advisory.org</li>
    <li><svg class="icon" viewBox="0 0 16 16"><path d="M8 0a5 5 0 0 0-5 5c0 4 5 11 5 11s5-7 5-11a5 5 0 0 0-5-5zm0 7a2 2 0 1 1 0-4 2 2 0 0 1 0 4z"/></svg>PO Box 318 Kelmscott NSW 2193 AUSTRALIA</li>
  </ul>
</section>

<section class="card card--back" aria-label="Business card back">
  <svg class="card__arc" width="640" height="366" viewBox="0 0 640 366" aria-hidden="true">
    <path d="M0 40 C 220 40, 420 70, 640 150" fill="none" stroke="var(--arc)" stroke-width="2"/>
    <path d="M0 48 C 220 48, 420 78, 640 158" fill="none" stroke="rgba(120,150,220,0.15)" stroke-width="6"/>
  </svg>
  <div class="company-name">Harbourline Advisory<br>Group</div>
  <div class="emblem" role="img" aria-label="Company emblem image"></div>
  <div class="badge badge--certification" role="img" aria-label="KESTRA 4 certification badge"></div>
  <div class="badge badge--partner" role="img" aria-label="QV Network Affiliate partner badge"></div>
</section>

</body>
</html>
```